Decking and Wooden Fencing Specialist Flyer Design

We are starting a new company offering decking installation, patios and wooden/stone fencing. We are looking for a flyer that gives professional impression, with an accent put on a high quality of services.

Industry/Entity Type

Fencing

```html
<!DOCTYPE html>
<html lang="en">
<head>
<meta charset="utf-8">
<title>Oakline Building Services – Decking and Fencing Flyer</title>
<link href="https://fonts.googleapis.com/css2?family=Anton&family=Questrial&display=swap" rel="stylesheet">
<style>
  :root {
    --bg: #dcb07a;
    --wood: #6b3a22;
    --wood-dark: #4e2816;
    --charcoal: #231f20;
    --cream: #f3e6d6;
    --tan: #d9a57c;
    --tan-light: #eecdb1;
    --deck-top: #4f7a3a;
    --deck-mid: #8a5a3e;
    --deck-low: #a0674a;
    --worker-a: #b59a78;
    --worker-b: #5a4a3e;
    --white: #ffffff;
  }
  * { margin: 0; padding: 0; box-sizing: border-box; }
  html, body { width: 1200px; height: 999px; overflow: hidden; }
  body { background: var(--bg); font-family: "Questrial", sans-serif; position: relative; }

  .flyer {
    position: absolute; left: 300px; top: 50px; width: 600px; height: 900px;
    background: var(--wood); overflow: hidden;
    box-shadow: 0 10px 30px rgba(60, 30, 10, 0.25);
  }

  .header { position: absolute; left: 0; top: 0; width: 600px; height: 95px;
    background: linear-gradient(180deg, var(--wood) 0%, var(--wood-dark) 100%); }
  .brand-box { position: absolute; left: 22px; top: 22px; width: 200px; height: 56px;
    background: var(--charcoal); display: flex; align-items: center; gap: 10px; padding-left: 16px; }
  .brand-mark { width: 14px; height: 14px; background: var(--tan); }
  .brand-name { font-size: 16px; color: var(--cream); }
  .header-title { position: absolute; left: 245px; top: 12px; font-family: "Anton", sans-serif;
    font-size: 44px; line-height: 1; color: var(--cream); letter-spacing: 0.5px; }
  .header-sub { position: absolute; left: 250px; top: 60px; font-size: 15px; letter-spacing: 9px;
    color: var(--tan-light); text-transform: uppercase; }

  .band { position: absolute; left: 0; width: 600px; height: 50px; background: var(--charcoal);
    color: var(--cream); font-size: 24px; line-height: 50px; padding-left: 26px; }
  .band--top { top: 95px; border-top: 3px solid var(--tan); }
  .band--mid { top: 425px; font-size: 23px; }

  .photo { position: absolute; left: 0; width: 600px; }
  .photo--deck { top: 145px; height: 280px;
    background: linear-gradient(180deg, var(--deck-top) 0%, #7b8a5a 30%, var(--deck-mid) 45%, var(--deck-low) 100%); }
  .photo--worker { top: 475px; height: 290px;
    background: linear-gradient(100deg, var(--worker-a) 0%, #8c7660 50%, var(--worker-b) 100%); }

  .sign { position: absolute; left: 32px; top: 190px; width: 210px; height: 110px;
    background: var(--charcoal); border: 6px solid var(--tan); color: var(--white);
    font-family: "Anton", sans-serif; font-size: 16px; padding: 12px 18px; }
  .sign li, .features li { list-style: none; }
  .sign li { display: flex; align-items: center; gap: 10px; line-height: 26px; }
  .sign li::before { content: ""; width: 7px; height: 7px; border: 2px solid var(--tan); border-radius: 50%; }

  .plaques { position: absolute; left: 270px; top: 300px; display: flex; flex-direction: column; gap: 8px; }
  .plaque { width: 220px; height: 30px; background: var(--tan-light); border: 2px solid var(--charcoal);
    border-radius: 3px; font-family: "Anton", sans-serif; font-size: 15px; color: var(--charcoal);
    display: flex; align-items: center; padding: 0 14px; gap: 10px; position: relative; }
  .plaque::before, .plaque::after { content: ""; width: 7px; height: 7px; border: 2px solid var(--charcoal); border-radius: 50%; }
  .plaque::after { position: absolute; right: 10px; }

  .features { position: absolute; left: 28px; top: 500px; width: 360px; height: 240px;
    background: rgba(35, 31, 32, 0.72); padding: 20px 24px; color: var(--cream); }
  .features-label { display: inline-block; background: var(--tan); color: var(--charcoal);
    font-family: "Anton", sans-serif; font-size: 18px; padding: 3px 22px; margin-left: -24px; }
  .features ul { margin-top: 10px; font-size: 20px; line-height: 30px; }

  .footer { position: absolute; left: 0; top: 765px; width: 600px; height: 135px;
    background: var(--wood); border-top: 3px solid var(--tan); }
  .call { position: absolute; right: 30px; top: 16px; font-family: "Anton", sans-serif; font-size: 34px;
    color: var(--white); }
  .call-label { color: var(--tan); margin-right: 10px; }
  .email { position: absolute; left: 30px; top: 72px; font-family: "Anton", sans-serif; font-size: 30px;
    color: var(--white); }
</style>
</head>
<body>
  <article class="flyer">
    <header class="header">
      <div class="brand-box">
        <span class="brand-mark"></span>
        <span class="brand-name">Oakline Building</span>
      </div>
      <div class="header-title">Oakline Building</div>
      <div class="header-sub">Services</div>
    </header>

    <div class="band band--top">Bespoke made decks and patios</div>

    <div class="photo photo--deck" role="img" aria-label="Photo of a finished timber deck with railing and trees behind"></div>

    <ul class="sign">
      <li>Quality Built</li>
      <li>Lowest Price</li>
      <li>Affordable Decks</li>
    </ul>

    <div class="plaques">
      <div class="plaque">High quality service</div>
      <div class="plaque">Our price Gurantee</div>
      <div class="plaque">Fencing Specialist</div>
    </div>

    <div class="band band--mid">Decking and Wooden Fencing Specialist</div>

    <div class="photo photo--worker" role="img" aria-label="Photo of a carpenter with a tool belt working on timber"></div>

    <section class="features">
      <span class="features-label">FEATURES</span>
      <ul>
        <li>Hurricane Rafter</li>
        <li>Calked And Leg Bolted</li>
        <li>Stairs</li>
        <li>Ledger Board</li>
        <li>Wooden Fencing</li>
      </ul>
    </section>

    <footer class="footer">
      <div class="call"><span class="call-label">Call</span>555-204-318</div>
      <div class="email">your emial here</div>
    </footer>
  </article>
</body>
</html>
```